Author/ Speaker Business Card design

I need a business card designed that will go with the branding that is already on my book and website. I like clean and straightforward, but I am not opposed to something more 'innovative'.

Target Market(s)

Colleges and Universities, educational institutions

Industry/Entity Type

Education

Contact Information for Business Card

Standard size. It should be able to be printed on good quality white or ivory paper.

Font styles to use
Sans Serif

Colors
0355a3

Requirements
Must have
• There's a blue on my website. It should have some blue. My logo is at the top. It should have the logo incorporated somewhere on it. My name, Author | Speaker | Teacher | Trainer, my phone number (+31 64-207 5819), my email address (milo@theboldlearner.example), Social media icons (twitter, Instagram, LinkedIn) with the addresses (twitter @writermilofenwick, Instagram - theboldlearner, LinkedIn - theboldlearner) By they way, the website is www.theboldlearner.example. There is a photo of the book on the website. Also, my full name is Milo Fenwick
Nice to have
• Try to use the font that is on the website and book. Also, if you could get that blue, that would be great.
Should not have
• My photo

```html
<!DOCTYPE html>
<html lang="en">
<head>
<meta charset="utf-8">
<title>Milo Fenwick – Business Card</title>
<link rel="stylesheet" href="https://fonts.googleapis.com/css2?family=Roboto:wght@400;500;700&display=swap">
<style>
  :root {
    --brand-blue: #0355a3;
    --band-blue: #0a52a0;
    --paper: #f4f4f3;
    --ink: #1f1f1f;
    --backdrop: #d9d9d9;
    --rule: #2a2a2a;
  }
  * { box-sizing: border-box; margin: 0; padding: 0; }
  html, body {
    width: 1198px; height: 1200px; overflow: hidden;
    background: var(--backdrop);
    font-family: "Roboto", Arial, sans-serif;
  }
  .card {
    position: absolute; left: 99px; top: 314px;
    width: 1000px; height: 572px;
    background: var(--paper);
    box-shadow: 0 2px 6px rgba(0,0,0,0.12);
    overflow: hidden;
  }
  .brand {
    position: absolute; top: 62px; left: 0; width: 100%;
    display: flex; justify-content: center; align-items: center; gap: 16px;
  }
  .brand-dot {
    width: 26px; height: 26px; border-radius: 50%;
    background: var(--brand-blue);
  }
  .brand-name {
    color: var(--brand-blue); font-weight: 700; font-size: 52px;
    letter-spacing: 0.5px;
  }
  .band {
    position: absolute; top: 172px; left: 0; width: 100%; height: 150px;
    background: var(--band-blue);
    color: #fff; text-align: center;
    display: flex; flex-direction: column; justify-content: center; gap: 10px;
  }
  .person-name {
    font-weight: 700; font-size: 40px; letter-spacing: 9px; text-transform: uppercase;
  }
  .person-roles {
    font-weight: 400; font-size: 24px; letter-spacing: 1.5px; text-transform: uppercase;
  }
  .contacts {
    position: absolute; top: 350px; left: 110px;
    list-style: none; display: flex; flex-direction: column; gap: 14px;
  }
  .contact {
    display: flex; align-items: center; gap: 16px;
    font-size: 24px; letter-spacing: 2.5px; color: var(--ink);
  }
  .contact svg { width: 22px; height: 22px; fill: var(--brand-blue); flex: none; }
  .rule {
    position: absolute; top: 484px; left: 110px; right: 60px;
    border-top: 2px solid var(--rule);
  }
  .socials {
    position: absolute; top: 506px; left: 110px; right: 60px;
    list-style: none; display: flex; justify-content: space-between;
  }
  .social {
    display: flex; align-items: center; gap: 12px;
    font-size: 24px; letter-spacing: 0.5px; color: var(--ink);
  }
  .social-mark {
    width: 16px; height: 16px; border-radius: 50%; background: var(--ink); flex: none;
  }
</style>
</head>
<body>
  <article class="card">
    <header class="brand">
      <span class="brand-dot"></span>
      <span class="brand-name">The Bold Learner</span>
    </header>

    <section class="band">
      <h1 class="person-name">Milo Fenwick</h1>
      <p class="person-roles">Author | Speaker | Teacher | Trainer</p>
    </section>

    <ul class="contacts">
      <li class="contact">
        <svg viewBox="0 0 24 24" aria-hidden="true"><path d="M6.6 10.8c1.4 2.8 3.8 5.1 6.6 6.6l2.2-2.2c.3-.3.7-.4 1-.2 1.1.4 2.3.6 3.6.6.6 0 1 .4 1 1V20c0 .6-.4 1-1 1C10.6 21 3 13.4 3 4c0-.6.4-1 1-1h3.5c.6 0 1 .4 1 1 0 1.3.2 2.5.6 3.6.1.3 0 .7-.2 1l-2.3 2.2z"/></svg>
        <span>+31 64-207 5819</span>
      </li>
      <li class="contact">
        <svg viewBox="0 0 24 24" aria-hidden="true"><path d="M2 5h20v14H2z M2 5l10 8 10-8" stroke="#f4f4f3" stroke-width="1.5"/></svg>
        <span>milo@theboldlearner.example</span>
      </li>
      <li class="contact">
        <svg viewBox="0 0 24 24" aria-hidden="true"><circle cx="12" cy="12" r="10"/><path d="M2 12h20M12 2c3 3 3 17 0 20M12 2c-3 3-3 17 0 20M4 7h16M4 17h16" stroke="#f4f4f3" stroke-width="1.2" fill="none"/></svg>
        <span>www.theboldlearner.example</span>
      </li>
    </ul>

    <div class="rule"></div>

    <ul class="socials">
      <li class="social"><span class="social-mark"></span><span>@writermilofenwick</span></li>
      <li class="social"><span class="social-mark"></span><span>theboldlearner</span></li>
      <li class="social"><span class="social-mark"></span><span>theboldlearner</span></li>
    </ul>
  </article>
</body>
</html>
```